Film Festival Poster Design Project

The 5th Annual Harwell Open Screen Festival will be taking place on November 12th in Wales at the Larkmoor Cinema, Newport.

It is an all day event and there will be an eclectic mix of films on show.

Target Market(s)

Students 18-25

Industry/Entity Type

Festival

Requirements
Must have
• Title: 5th Harwell Open Screen Festival

Date: Saturday 19th November 2011

Place: Larkmoor Theatre & Cinema, Aberhallow, Wales

Must include the text: BUY TICKETS ONLINE AT WWW.REELGATHERHALL.EXAMPLE

Sponsors & Festival Logo's must be included.
Nice to have
• As the festival is based in Wales, it would be nice to have a slightly Welsh tone to the poster, or a British feel.

```html
<!DOCTYPE html>
<html lang="en">
<head>
<meta charset="utf-8">
<title>5th Harwell Open Screen Festival</title>
<link rel="stylesheet" href="https://fonts.googleapis.com/css2?family=UnifrakturMaguntia&family=PT+Sans+Narrow:wght@400;700&family=PT+Serif:wght@400;700&display=swap">
<style>
  :root {
    --ink: #000000;
    --paper: #ffffff;
    --panel-dark: #000000;
  }
  html, body {
    margin: 0;
    padding: 0;
    overflow: hidden;
    background: var(--paper);
  }
  .poster {
    position: relative;
    width: 1200px;
    height: 900px;
    background: var(--paper);
    color: var(--ink);
    overflow: hidden;
    font-family: "PT Sans Narrow", sans-serif;
  }
  .festival-title {
    position: absolute;
    top: 16px;
    left: 0;
    width: 1200px;
    margin: 0;
    text-align: center;
    font-family: "UnifrakturMaguntia", serif;
    font-weight: 400;
    font-size: 74px;
    line-height: 1;
  }
  .organiser-name {
    position: absolute;
    left: 24px;
    top: 150px;
    margin: 0;
    font-family: "PT Sans Narrow", sans-serif;
    font-weight: 700;
    font-size: 190px;
    line-height: 166px;
    letter-spacing: 4px;
    color: var(--ink);
  }
  .organiser-name span { display: block; }
  .ticket-button {
    position: absolute;
    left: 774px;
    top: 240px;
    width: 282px;
    height: 131px;
    background: var(--panel-dark);
    color: var(--paper);
    display: flex;
    align-items: center;
    justify-content: center;
    text-align: center;
    font-family: "PT Serif", serif;
    font-size: 32px;
    line-height: 44px;
  }
  .ticket-info {
    position: absolute;
    left: 690px;
    top: 392px;
    width: 460px;
    text-align: center;
    font-family: "PT Sans Narrow", sans-serif;
    font-size: 25px;
  }
  .ticket-info p { margin: 0; }
  .ticket-info .ticket-url { margin-top: 26px; }
  .event-details {
    position: absolute;
    left: 692px;
    top: 590px;
    font-size: 33px;
    line-height: 38px;
  }
  .event-details p { margin: 0; }
  .event-details .indent { padding-left: 96px; }
  .sponsor-label {
    position: absolute;
    left: 10px;
    top: 680px;
    margin: 0;
    font-family: "PT Serif", serif;
    font-weight: 700;
    font-size: 25px;
  }
  .sponsor-row {
    position: absolute;
    left: 0;
    top: 722px;
    width: 1200px;
    height: 178px;
  }
  .sponsor {
    position: absolute;
    top: 0;
    height: 178px;
    display: flex;
    flex-direction: column;
    align-items: center;
    justify-content: center;
    text-align: center;
    font-family: "PT Sans Narrow", sans-serif;
    font-weight: 700;
  }
  .sponsor.dark { background: var(--panel-dark); color: var(--paper); }
  .sponsor.light { background: var(--paper); color: var(--ink); }
  .sponsor-ashgrove { left: 0; width: 278px; }
  .sponsor-lumenvale { left: 285px; width: 293px; }
  .sponsor-fenwick { left: 585px; width: 316px; }
  .sponsor-festival { left: 908px; width: 292px; }
  .sponsor-name { font-size: 30px; line-height: 1.1; letter-spacing: 1px; }
  .sponsor-url { font-weight: 400; font-size: 13px; margin-top: 8px; }
</style>
</head>
<body>
<main class="poster">
  <h1 class="festival-title">5th Harwell Open Screen Festival</h1>

  <h2 class="organiser-name"><span>REEL</span><span>GATHER</span><span>HALL</span></h2>

  <div class="ticket-button">BUY TICKETS<br>ONLINE</div>

  <div class="ticket-info">
    <p>BUY TICKETS ONLINE AT</p>
    <p class="ticket-url">WWW.REELGATHERHALL.EXAMPLE</p>
  </div>

  <div class="event-details">
    <p>Date: Saturday 19th November 2011</p>
    <p>Place: Larkmoor Theatre &amp; Cinema,</p>
    <p class="indent">Aberhallow, Wales</p>
  </div>

  <p class="sponsor-label">SPONSERED By</p>

  <section class="sponsor-row">
    <div class="sponsor dark sponsor-ashgrove">
      <div class="sponsor-name">ASHGROVE PICTURES</div>
      <div class="sponsor-url">www.ashgrovepictures.example</div>
    </div>
    <div class="sponsor light sponsor-lumenvale">
      <div class="sponsor-name">LUMENVALE</div>
    </div>
    <div class="sponsor dark sponsor-fenwick">
      <div class="sponsor-name">fenwick digital media</div>
    </div>
    <div class="sponsor light sponsor-festival">
      <div class="sponsor-name">HARWELL OPEN<br>SCREEN FESTIVAL</div>
    </div>
  </section>
</main>
</body>
</html>
```